General Power Point Presentation Pack

Hello Designers,

I am after a professional looking Microsoft PowerPoint deck that can be used for our corporate presentations. The pack should include a:

Title Page
Tittle and Content Page
Section Header Sheet
Two Content Page
Title Only Page
Blank Page
Content with Caption Page
Picture with Caption Page

I have included my brand guidelines and colours. I have also included some photos you may be able to use. Can you please ensure the pack has page numbering and that when you print it that it can be printed to full A4 Page.

Industry/Entity Type

Property Development & Construction

Requirements
Must have
• Prefer a white or very light coloured background

```html
<!DOCTYPE html>
<html lang="en">
<head>
<meta charset="utf-8">
<title>Keystone Group – Presentation Pack</title>
<link href="https://fonts.googleapis.com/css2?family=Roboto:wght@300;400;500;700&display=swap" rel="stylesheet">
<style>
:root{
  --bg:#e9e9e9;
  --page:#ffffff;
  --ink:#141414;
  --body:#6b6b6b;
  --orange:#d9582b;
  --blue:#2f6a9e;
  --teal:#8cc7b0;
  --grey:#6a6a6a;
  --beige:#f2eadc;
  --tan:#d6b58a;
  --sky:#cfe3f1;
  --mist:#e2e2e2;
}
*{box-sizing:border-box;margin:0;padding:0}
html,body{width:1200px;height:2194px;overflow:hidden;background:var(--bg);font-family:"Roboto",Arial,sans-serif;color:var(--body)}
.sheet{position:relative;width:1200px;height:2194px}
.page{position:absolute;width:337px;height:487px;background:var(--page);box-shadow:6px 10px 22px rgba(0,0,0,.18);overflow:hidden}
.c1{left:49px}.c2{left:431px}.c3{left:813px}
.r1{top:60px}.r2{top:583px}.r3{top:1107px}.r4{top:1631px}
.stripe{position:absolute;top:0;left:31px;width:276px;height:3px;display:flex;z-index:3}
.stripe i{flex:1}
.stripe i:nth-child(1){background:var(--orange)}
.stripe i:nth-child(2){background:var(--beige)}
.stripe i:nth-child(3){background:var(--grey)}
.stripe i:nth-child(4){background:var(--tan)}
.stripe i:nth-child(5){background:var(--teal)}
.brand{position:absolute;top:19px;right:27px;display:flex;align-items:center;gap:3px;font-weight:500;font-size:11px;color:var(--orange);z-index:3}
.brand.left{left:29px;right:auto}
.brand.light{color:#fff}
.brand b{display:block;width:8px;height:8px;background:currentColor}
.foot{position:absolute;bottom:9px;left:33px;right:33px;display:flex;justify-content:space-between;font-size:6.5px;color:#444;z-index:3}
.title{position:absolute;font-weight:700;color:var(--ink);line-height:.92;letter-spacing:-.6px;text-transform:uppercase}
.title span{color:var(--orange)}
.title .blue{color:var(--blue)}
.title .teal{color:var(--teal)}
.copy{position:absolute;font-size:6px;line-height:1.45;text-align:justify;color:var(--body);font-weight:300}
.copy p+p{margin-top:6px}
.copy strong{font-weight:500;color:#333}
.photo{position:absolute;background:linear-gradient(180deg,#a89fbf 0%,#d9b9c2 40%,#9b8a80 70%,#4b4642 100%)}
.photo.day{background:linear-gradient(180deg,#b9d2e6 0%,#dfe7ea 40%,#9d8f82 70%,#4f5d46 100%)}
.photo.room{background:linear-gradient(180deg,#efece6 0%,#e0d9ce 55%,#b9a891 100%)}
.photo.site{background:linear-gradient(180deg,#7fa8d4 0%,#b9cde0 45%,#4d6d92 75%,#2f4a6e 100%)}
.h{font-size:8px;font-weight:500;color:#222}
</style>
</head>
<body>
<main class="sheet">

<!-- Page 1 -->
<section class="page c1 r1">
  <div class="stripe"><i></i><i></i><i></i><i></i><i></i></div>
  <div class="brand"><b></b>Keystone</div>
  <h1 class="title" style="left:29px;top:68px;font-size:27px">About<br><span>Keystone Group</span></h1>
  <div class="copy" style="left:33px;top:140px;width:270px">
    <p>Keystone is a highly acclaimed Australian property developer specializing in residential and commercial properties.</p>
    <p>With over 20 years of experience, Keystone has successfully completed billions of dollars worth of residential, commercial, retail, industrial, medical and club developments. It has earned a reputation for delivering high-quality property developments, each with its own distinctive character that has captured the imagination of owner-occupiers and investors alike.</p>
  </div>
  <div class="copy" style="left:33px;top:242px;width:120px">
    <p>One of Sydney's most consistent and successful property developers, Keystone is known for excellence in design, construction and customer care and deeply committed to building our future communities.</p>
    <p>All our developments are backed by an industry-leading Quality Guarantee, which includes a 10-year Extended Structural Warranty* on building structure, exceeding NSW Government's 6-year statutory requirement.</p>
  </div>
  <div class="photo" style="left:169px;top:244px;width:141px;height:158px" role="img" aria-label="Apartment building at dusk"></div>
  <svg style="position:absolute;left:33px;top:417px" width="40" height="40" viewBox="0 0 40 40"><circle cx="20" cy="20" r="18" fill="none" stroke="#e8b49f" stroke-width="1.5"/><circle cx="20" cy="20" r="12" fill="#fbeee8"/></svg>
  <div class="copy" style="left:82px;top:422px;width:225px;font-size:4.3px;font-style:italic;line-height:1.3">* The 10-year warranty is transferable to any subsequent owner during the life of the warranty and applies to all Keystone buildings completed after 1 January 2020. The warranty is limited to load bearing elements and does not apply if the structure is modified or altered after handover by any party.</div>
  <div class="foot"><span>keystonegr.com</span><span>1</span></div>
</section>

<!-- Page 2 -->
<section class="page c2 r1">
  <div class="stripe"><i></i><i></i><i></i><i></i><i></i></div>
  <div class="photo site" style="left:0;top:0;width:337px;height:164px" role="img" aria-label="Site engineer in hard hat facing a tower under construction"></div>
  <div class="brand light"><b></b>Keystone</div>
  <h1 style="position:absolute;left:29px;top:174px;font-size:26px;font-weight:500;color:var(--orange)">Content</h1>
  <div style="position:absolute;left:56px;top:248px;width:270px;font-size:6.3px;line-height:1.85">
    <div style="display:flex;padding-bottom:6px;border-bottom:1px solid #ddd"><span style="width:109px;color:var(--orange)">13:00 – 13:15</span><span>Opening ceremony</span></div>
    <div style="display:flex;padding:7px 0;border-bottom:1px solid #ddd"><span style="width:109px;color:var(--orange)">13:15 – 14:00<br>14:00 – 15:00</span><span>Speakers introduction<br>Opening</span></div>
    <div style="display:flex;padding:7px 0;border-bottom:1px solid #ddd"><span style="width:109px;color:var(--orange)">15:45 – 16:00</span><span>Break</span></div>
    <div style="display:flex;padding:7px 0;border-bottom:1px solid #ddd"><span style="width:109px;color:var(--orange)">16:00 – 16:30<br>16:30 – 17:00<br>17:00 – 17:30</span><span>Speaker - Paul Whitfield<br>Speaker - Leo Marsh<br>Speaker - Dana Corr</span></div>
    <div style="display:flex;padding:7px 0"><span style="width:109px;color:var(--orange)">17:30 – 19:00</span><span>Conclusions Q&amp;A</span></div>
  </div>
  <div class="foot"><span>keystonegr.com</span><span>2</span></div>
</section>

<!-- Page 3 -->
<section class="page c3 r1">
  <div class="stripe" style="width:150px"><i></i><i></i><i></i><i></i><i></i></div>
  <div class="brand left"><b></b>Keystone</div>
  <h2 class="title" style="left:29px;top:55px;font-size:18px">Lorem ipsum<br><span class="blue">is simple<br>dummy text</span></h2>
  <div class="copy" style="left:33px;top:128px;width:131px"><strong>Lorem Ipsum</strong> is simply dummy text of the printing and typesetting industry. Lorem Ipsum has been the industry's standard dummy text ever since the 1500s, when an unknown printer took a galley of type and scrambled it to make a type specimen book. It has survived not only five centuries, but also the leap into electronic typesetting, remaining essentially unchanged. It was</div>
  <h2 class="title" style="left:29px;top:275px;font-size:18px">Lorem ipsum<br><span class="teal">is simple<br>dummy text</span></h2>
  <div class="copy" style="left:33px;top:355px;width:131px"><strong>Lorem Ipsum</strong> is simply dummy text of the printing and typesetting industry. Lorem Ipsum has been the industry's standard dummy text ever since the 1500s, when an unknown printer took a galley of type and scrambled it to make a type specimen book. It has survived not only five centuries, but also the leap into electronic typesetting, remaining essentially unchanged. It was</div>
  <div class="photo day" style="left:187px;top:0;width:150px;height:80px" role="img" aria-label="Apartment building exterior"></div>
  <div class="photo room" style="left:187px;top:82px;width:150px;height:78px" role="img" aria-label="Open plan kitchen interior"></div>
  <div class="photo day" style="left:187px;top:162px;width:150px;height:78px" role="img" aria-label="Townhouse facade"></div>
  <div class="photo day" style="left:187px;top:242px;width:150px;height:78px" role="img" aria-label="Modern apartment block"></div>
  <div class="photo day" style="left:187px;top:322px;width:150px;height:82px" role="img" aria-label="Apartment building with gardens"></div>
  <div class="photo room" style="left:187px;top:406px;width:150px;height:81px" role="img" aria-label="Living and dining interior"></div>
  <div class="foot" style="right:180px"><span>keystonegr.com</span><span></span></div>
</section>

<!-- Page 4 -->
<section class="page c1 r2">
  <div class="stripe"><i></i><i></i><i></i><i></i><i></i></div>
  <div class="brand"><b></b>Keystone</div>
  <h2 class="title" style="left:29px;top:79px;font-size:21px">Lorem<br>ipsum <span>is<br>simple<br>dummy<br>text</span></h2>
  <div class="copy" style="left:33px;top:204px;width:120px;font-size:5.8px">
    <p><strong>Lorem Ipsum</strong> is simply dummy text of the printing and typesetting industry. Lorem Ipsum has been the industry's standard dummy text ever since the 1500s, when an unknown printer took a galley of type and scrambled it to make a type specimen book. It has survived not only five centuries, but also the leap into electronic typesetting, remaining essentially unchanged. It was</p>
    <p>Lorem Ipsum is simply dummy text of the printing and typesetting industry. Lorem Ipsum has been the industry's standard dummy text ever since the 1500s, when an unknown printer took a galley of type and scrambled it to make a type specimen book. It has survived not only five centuries, but also the leap into electronic typesetting, remaining essentially unchanged. It is a long established fact that a reader will be distracted by the</p>
  </div>
  <div style="position:absolute;left:169px;top:71px;width:140px;height:115px;background:var(--sky);border-top:2px solid var(--blue);padding:22px 18px"><div class="h">Strategy One</div><div class="copy" style="position:static;margin-top:8px;text-align:left;font-size:6px;line-height:1.9">Lorem Ipsum is simply dummy text of the printing and typesetting industry. Lorem Ipsum has been the industry's standard dummy text</div></div>
  <div style="position:absolute;left:169px;top:201px;width:140px;height:112px;background:var(--mist);border-top:2px solid var(--grey);padding:22px 18px"><div class="h">Strategy Two</div><div class="copy" style="position:static;margin-top:8px;text-align:left;font-size:6px;line-height:1.9">Lorem Ipsum is simply dummy text of the printing and typesetting industry. Lorem Ipsum has been the industry's standard dummy text</div></div>
  <div style="position:absolute;left:169px;top:326px;width:140px;height:112px;background:var(--beige);border-top:2px solid var(--tan);padding:22px 18px"><div class="h">Strategy Three</div><div class="copy" style="position:static;margin-top:8px;text-align:left;font-size:6px;line-height:1.9">Lorem Ipsum is simply dummy text of the printing and typesetting industry. Lorem Ipsum has been the industry's standard dummy text</div></div>
  <div class="foot"><span>keystonegr.com</span><span>4</span></div>
</section>

<!-- Page 5 -->
<section class="page c2 r2">
  <div class="stripe" style="width:140px"><i></i><i></i><i></i><i></i><i></i></div>
  <div class="brand left"><b></b>Keystone</div>
  <h2 class="title" style="left:29px;top:80px;font-size:21px">Your two<br>image<br><span>title<br>layout<br>here</span></h2>
  <div class="copy" style="left:33px;top:204px;width:121px;font-size:5.8px">
    <p><strong>Lorem Ipsum</strong> is simply dummy text of the printing and typesetting industry. Lorem Ipsum has been the industry's standard dummy text ever since the 1500s, when an unknown printer took a galley of type and scrambled it to make a type specimen book. It has survived not only five centuries, but also the leap into electronic typesetting, remaining essentially unchanged. It was</p>
    <p>Lorem Ipsum is simply dummy text of the printing and typesetting industry. Lorem Ipsum has been the industry's standard dummy text ever since the 1500s, when an unknown printer took a galley of type and scrambled it to make a type specimen book. It has survived not only five centuries, but also the leap into electronic typesetting, remaining essentially unchanged. It is a long established fact that a reader will be distracted by the</p>
  </div>
  <div class="photo" style="left:169px;top:13px;width:168px;height:225px" role="img" aria-label="Apartment entrance with palm trees at dusk"></div>
  <div class="photo" style="left:169px;top:244px;width:168px;height:225px" role="img" aria-label="Apartment building on street corner at dusk"></div>
  <div class="foot"><span>keystonegr.com</span><span>5</span></div>
</section>

<!-- Page 6 -->
<section class="page c3 r2">
  <div class="stripe"><i></i><i></i><i></i><i></i><i></i></div>
  <div class="brand"><b></b>Keystone</div>
  <h2 class="title" style="left:29px;top:56px;font-size:20px;letter-spacing:-1px">Your title content for a<br><span>bullets slide creative</span></h2>
  <svg style="position:absolute;left:0;top:0" width="337" height="487" viewBox="0 0 337 487">
    <g fill="none" stroke="#fff" stroke-width="1.3" stroke-linecap="round">
      <circle cx="75" cy="148" r="20" fill="#8cc7b0" stroke="none"/><path d="M69 148l4 4 8-8"/>
      <circle cx="75" cy="210" r="20" fill="#6a6a6a" stroke="none"/><path d="M69 210l4 4 8-8"/>
      <circle cx="75" cy="272" r="20" fill="#d9582b" stroke="none"/><path d="M69 272l4 4 8-8"/>
      <circle cx="75" cy="334" r="20" fill="#2f6a9e" stroke="none"/><path d="M69 334l4 4 8-8"/>
      <circle cx="75" cy="396" r="20" fill="#f2eadc" stroke="none"/><path d="M69 396l4 4 8-8" stroke="#555"/>
    </g>
  </svg>
  <div style="position:absolute;left:109px;top:138px;width:200px;font-size:6px;line-height:1.3">
    <div style="height:62px"><div style="color:var(--teal);font-size:7.5px">Lorem Ipsum is simply dummy text</div><div style="margin-top:4px;font-size:5px">Lorem Ipsum is simply dummy text of the printing and typesetting industry. Lorem Ipsum has been the industry's standard dummy text</div></div>
    <div style="height:62px"><div style="color:#444;font-size:7.5px">Lorem Ipsum is simply dummy text</div><div style="margin-top:4px;font-size:5px">Lorem Ipsum is simply dummy text of the printing and typesetting industry. Lorem Ipsum has been the industry's standard dummy text</div></div>
    <div style="height:62px"><div style="color:var(--orange);font-size:7.5px">Lorem Ipsum is simply dummy text</div><div style="margin-top:4px;font-size:5px">Lorem Ipsum is simply dummy text of the printing and typesetting industry. Lorem Ipsum has been the industry's standard dummy text</div></div>
    <div style="height:62px"><div style="color:var(--blue);font-size:7.5px">Lorem Ipsum is simply dummy text</div><div style="margin-top:4px;font-size:5px">Lorem Ipsum is simply dummy text of the printing and typesetting industry. Lorem Ipsum has been the industry's standard dummy text</div></div>
    <div><div style="color:#444;font-size:7.5px">Lorem Ipsum is simply dummy text</div><div style="margin-top:4px;font-size:5px">Lorem Ipsum is simply dummy text of the printing and typesetting industry. Lorem Ipsum has been the industry's standard dummy text</div></div>
  </div>
  <div class="foot"><span>keystonegr.com</span><span>6</span></div>
</section>

<!-- Page 7 -->
<section class="page c1 r3">
  <div class="stripe"><i></i><i></i><i></i><i></i><i></i></div>
  <div class="brand"><b></b>Keystone</div>
  <h2 class="title" style="left:29px;top:47px;font-size:20px;letter-spacing:-1px">Your title<br>content for<br><span>a portfolio<br>slide</span></h2>
  <div class="copy" style="left:33px;top:148px;width:131px">
    <p><strong>Lorem Ipsum</strong> is simply dummy text of the printing and typesetting industry. Lorem Ipsum has been the industry's standard dummy text ever since the 1500s, when an unknown printer took a galley of type and scrambled it to make a type specimen book. It has survived not only five centuries, but also the leap into electronic typesetting, remaining essentially unchanged. It was</p>
    <p>Lorem Ipsum is simply dummy text of the printing and typesetting industry. Lorem Ipsum has been the industry's</p>
  </div>
  <div class="photo day" style="left:176px;top:39px;width:139px;height:77px" role="img" aria-label="Apartment complex exterior"></div>
  <div class="photo room" style="left:176px;top:123px;width:139px;height:77px" role="img" aria-label="Kitchen interior"></div>
  <div class="photo day" style="left:176px;top:207px;width:139px;height:77px" role="img" aria-label="Townhouse row"></div>
  <div class="photo day" style="left:29px;top:291px;width:139px;height:77px" role="img" aria-label="Apartment entrance with gardens"></div>
  <div class="photo day" style="left:176px;top:291px;width:139px;height:77px" role="img" aria-label="Modern residential block"></div>
  <div class="photo room" style="left:29px;top:375px;width:139px;height:77px" role="img" aria-label="Open plan living space"></div>
  <div class="photo day" style="left:176px;top:375px;width:139px;height:77px" role="img" aria-label="Terrace apartment facade"></div>
  <div class="foot"><span>keystonegr.com</span><span>7</span></div>
</section>

<!-- Page 8 -->
<section class="page c2 r3">
  <div class="photo" style="left:0;top:0;width:337px;height:315px" role="img" aria-label="Apartment tower at dusk with landscaped frontage"></div>
  <div class="stripe"><i></i><i></i><i></i><i></i><i></i></div>
  <div class="brand light"><b></b>Keystone</div>
  <h2 class="title" style="left:29px;top:57px;font-size:21px;color:#fff;opacity:.9;letter-spacing:-1px">Your title slide<br>content here</h2>
  <div style="position:absolute;left:0;top:315px;width:337px;height:172px;background:var(--orange);padding:22px 47px 0 47px;color:#fff">
    <div style="font-size:9px;font-weight:500">What is Lorem Ipsum?</div>
    <div class="copy" style="position:static;margin-top:10px;color:#fbe3d8;font-size:6px;line-height:1.9">Lorem Ipsum is simply dummy text of the printing and typesetting industry. Lorem Ipsum has been the industry's standard dummy text ever since the 1500s, when an unknown printer took a galley of type and scrambled it to make a type specimen book. It has survived not only five centuries, but also the leap into electronic typesetting, remaining essentially unchanged. It was popularised in the 1960s with the release of Letraset sheets containing Lorem Ipsum passages, and more recently with desktop publishing software like Aldus PageMaker including versions of Lorem Ipsum.</div>
  </div>
</section>

<!-- Page 9 -->
<section class="page c3 r3">
  <div class="stripe"><i></i><i></i><i></i><i></i><i></i></div>
  <div class="brand"><b></b>Keystone</div>
  <h2 class="title" style="left:29px;top:79px;font-size:20px;letter-spacing:-1px">Your title content<br><span>for a solo text slide</span></h2>
  <div style="position:absolute;left:29px;top:166px;width:270px">
    <div class="h">What is Lorem Ipsum?</div>
    <div class="copy" style="position:static;margin-top:9px;font-size:6.2px;line-height:1.85;color:#555">Lorem Ipsum is simply dummy text of the printing and typesetting industry. Lorem Ipsum has been the industry's standard dummy text ever since the 1500s, when an unknown printer took a galley of type and scrambled it to make a type specimen book. It has survived not only five centuries, but also the leap into electronic typesetting, remaining essentially unchanged. It was popularized in the 1960s with the release of Letraset sheets containing Lorem Ipsum passages, and more recently with desktop publishing software like Aldus PageMaker including versions of Lorem Ipsum.</div>
    <div class="h" style="margin-top:9px">Why do we use it?</div>
    <div class="copy" style="position:static;margin-top:9px;font-size:6.2px;line-height:1.85;color:#555">It is a long established fact that a reader will be distracted by the readable content of a page when looking at its layout. The point of using Lorem Ipsum is that it has a more-or-less normal distribution of letters, as opposed to using 'Content here, content here', making it look like readable English. Many desktop publishing packages and web page editors now use Lorem Ipsum as their default model text, and a search for 'lorem ipsum' will uncover many web sites still in their infancy. Various versions have evolved over the years, sometimes by accident, sometimes on purpose (injected humour and the like).</div>
  </div>
  <div class="foot"><span>keystonegr.com</span><span>9</span></div>
</section>

<!-- Page 10 -->
<section class="page c1 r4">
  <div class="photo room" style="left:0;top:0;width:337px;height:243px" role="img" aria-label="Bright kitchen and dining interior"></div>
  <div class="stripe"><i></i><i></i><i></i><i></i><i></i></div>
  <div class="brand light"><b></b>Keystone</div>
  <h2 class="title" style="left:33px;top:58px;font-size:21px;color:#fff;opacity:.9;letter-spacing:-1px">Your title slide<br>content here</h2>
  <div style="position:absolute;left:0;top:243px;width:337px;height:37px;background:var(--orange);display:flex;justify-content:space-around;align-items:center;color:#fff;font-size:14px;font-weight:500;padding:0 14px"><span>+ 5000</span><span>+50256</span><span>+ 502200</span></div>
  <div style="position:absolute;left:22px;top:294px;width:293px;display:flex;gap:12px">
    <div style="flex:1"><div style="font-size:7px;color:#444">What is Lorem Ipsum?</div><div class="copy" style="position:static;margin-top:9px;font-size:6px;line-height:1.9;color:#444">Lorem Ipsum is simply dummy text of the printing and typesetting industry. Lorem Ipsum has been the industry's standard dummy text ever since the 1500s, when an unknown printer took a galley of type and scrambled it to make a</div></div>
    <div style="flex:1"><div style="font-size:7px;color:var(--orange)">What is Lorem Ipsum?</div><div class="copy" style="position:static;margin-top:9px;font-size:6px;line-height:1.9;color:#444">Lorem Ipsum is simply dummy text of the printing and typesetting industry. Lorem Ipsum has been the industry's standard dummy text ever since the 1500s, when an unknown printer took a galley of type and scrambled it to make a</div></div>
    <div style="flex:1"><div style="font-size:7px;color:var(--blue)">What is Lorem Ipsum?</div><div class="copy" style="position:static;margin-top:9px;font-size:6px;line-height:1.9;color:#444">Lorem Ipsum is simply dummy text of the printing and typesetting industry. Lorem Ipsum has been the industry's standard dummy text ever since the 1500s, when an unknown printer took a galley of type and scrambled it to make a</div></div>
  </div>
  <div class="foot"><span>keystonegr.com</span><span>10</span></div>
</section>

<!-- Page 11 -->
<section class="page c2 r4">
  <div class="stripe"><i></i><i></i><i></i><i></i><i></i></div>
  <div class="brand"><b></b>Keystone</div>
  <h2 class="title" style="left:29px;top:79px;font-size:20px;letter-spacing:-1px">Your title content<br><span>for a data chart slide</span></h2>
  <svg style="position:absolute;left:55px;top:155px" width="82" height="270" viewBox="0 0 82 270">
    <g fill="none" stroke-width="9">
      <circle cx="41" cy="41" r="34" stroke="#f2eadc"/>
      <circle cx="41" cy="41" r="34" stroke="#d6b58a" stroke-dasharray="42.7 213.6" transform="rotate(-90 41 41)"/>
      <circle cx="41" cy="135" r="34" stroke="#f2eadc"/>
      <circle cx="41" cy="135" r="34" stroke="#2f6a9e" stroke-dasharray="85.5 213.6" transform="rotate(-90 41 135)"/>
      <circle cx="41" cy="229" r="34" stroke="#f2eadc"/>
      <circle cx="41" cy="229" r="34" stroke="#8cc7b0" stroke-dasharray="170.9 213.6" transform="rotate(-90 41 229)"/>
    </g>
    <g font-family="Roboto, Arial, sans-serif" font-weight="700" font-size="15" fill="#141414" text-anchor="middle">
      <text x="41" y="46">20%</text><text x="41" y="140">40%</text><text x="41" y="234">80%</text>
    </g>
  </svg>
  <div style="position:absolute;left:151px;top:165px;width:150px;font-size:6px;line-height:1.9;color:#444">
    <div style="height:94px"><div style="font-size:8px;color:var(--tan)">What is Lorem Ipsum?</div><div style="margin-top:8px">Lorem Ipsum is simply dummy text of the printing and typesetting industry. Lorem Ipsum has been the industry's standard</div></div>
    <div style="height:94px;padding-left:4px"><div style="font-size:8px;color:var(--blue)">What is Lorem Ipsum?</div><div style="margin-top:8px">Lorem Ipsum is simply dummy text of the printing and typesetting industry. Lorem Ipsum has been the industry's standard</div></div>
    <div style="padding-left:4px"><div style="font-size:8px;color:var(--teal)">What is Lorem Ipsum?</div><div style="margin-top:8px">Lorem Ipsum is simply dummy text of the printing and typesetting industry. Lorem Ipsum has been the industry's standard</div></div>
  </div>
  <div class="foot"><span>keystonegr.com</span><span>11</span></div>
</section>

<!-- Page 12 -->
<section class="page c3 r4">
  <div class="stripe"><i></i><i></i><i></i><i></i><i></i></div>
  <div class="brand"><b></b>Keystone</div>
  <h2 class="title" style="left:29px;top:79px;font-size:20px;letter-spacing:-1px">Your title content<br><span>for a table data chart</span></h2>
  <div style="position:absolute;left:33px;top:134px;width:270px">
    <div class="h">What is Lorem Ipsum?</div>
    <div class="copy" style="position:static;margin-top:7px;font-size:6px;line-height:1.85;color:#444">Lorem Ipsum is simply dummy text of the printing and typesetting industry. Lorem Ipsum has been the industry's standard dummy text ever since the 1500s, when an unknown printer took a galley of type and scrambled it to make a type specimen book. It has survived not only five centuries, but also the leap into electronic typesetting, remaining essentially unchanged. It was popularized in the 1960s with</div>
  </div>
  <table style="position:absolute;left:29px;top:232px;width:280px;border-collapse:collapse;font-size:6px;color:#333">
    <colgroup><col style="width:100px"><col><col><col></colgroup>
    <tbody>
      <tr style="height:32px;border-bottom:1px solid #e6e6e6"><td>Web design services and consultancy</td><td style="text-align:right">$13,000.00</td><td style="text-align:right">$8,000.00</td><td style="text-align:right;color:var(--orange)">$21,000.00</td></tr>
      <tr style="height:32px;border-bottom:1px solid #e6e6e6"><td>Hosting services / 24 months</td><td style="text-align:right">$28,000.00</td><td style="text-align:right">$3,000.00</td><td style="text-align:right;color:var(--orange)">$13,000.00</td></tr>
      <tr style="height:32px;border-bottom:1px solid #e6e6e6"><td>Template services</td><td style="text-align:right">$12,000.00</td><td style="text-align:right">$13,000.00</td><td style="text-align:right;color:var(--orange)">$15,000.00</td></tr>
      <tr style="height:32px;border-bottom:1px solid #e6e6e6"><td>Hosting services / 24 months</td><td style="text-align:right">$8,000.00</td><td style="text-align:right">$56,000.00</td><td style="text-align:right;color:var(--orange)">$18,000.00</td></tr>
      <tr style="height:32px;border-bottom:1.5px solid var(--orange)"><td>Web design services and consultancy</td><td style="text-align:right">$128,000.00</td><td style="text-align:right">$1,000.00</td><td style="text-align:right;color:var(--orange)">$25,000.00</td></tr>
      <tr style="height:30px;font-weight:500"><td>TOTAL</td><td style="text-align:right">$250,000.00</td><td style="text-align:right">$86,000.00</td><td style="text-align:right;color:var(--blue)">$13,000.00</td></tr>
    </tbody>
  </table>
  <div class="foot"><span>keystonegr.com</span><span>12</span></div>
</section>

</main>
</body>
</html>
```